Very personalised Wedding Invitation

I want a wedding invitation very unique and personalised with the menus, ceremony time table and thank you cards. I want a mix of a nice traditional style with indian style touch. I don't want a colourful invitation, it can have max. two different colours.

The bride's name is Miranda and the groom's name is Rohan

Reason: None of the designs submitted are what I am looking for

Target Market(s)

Invitations, personalised invitations,

Industry/Entity Type

Wedding

Logo Text

Our initials R&M To use in our wedding things

Font styles to use
Decorative
Script

Requirements
Must have
• -
Nice to have
• I would like a chic design with a bit of indian style
Should not have
• --

```html
<!DOCTYPE html>
<html lang="en">
<head>
<meta charset="utf-8">
<title>Miranda &amp; Rohan — Wedding Invitation</title>
<link rel="stylesheet" href="https://fonts.googleapis.com/css2?family=Pinyon+Script&display=swap">
<style>
  :root {
    --plum: #5c246d;
    --gold: #dcb46e;
    --ivory: #ffffff;
    --paper: #ffffff;
  }
  html, body {
    margin: 0;
    padding: 0;
    overflow: hidden;
    background: var(--paper);
  }
  .artboard {
    position: relative;
    width: 1200px;
    height: 993px;
    overflow: hidden;
    background: var(--paper);
    font-family: "Pinyon Script", cursive;
  }
  .invitation {
    position: absolute;
    left: 56px;
    top: 62px;
    width: 600px;
    height: 840px;
    background: var(--plum);
    overflow: hidden;
  }
  .mehndi-corner {
    position: absolute;
  }
  .mehndi-corner--top {
    left: 0;
    top: 0;
    width: 256px;
    height: 286px;
    background: radial-gradient(circle at 0 0, rgba(220,180,110,0.85) 0%, rgba(220,180,110,0.55) 55%, rgba(220,180,110,0) 100%);
    border-bottom-right-radius: 100% 100%;
  }
  .mehndi-corner--bottom {
    right: 0;
    bottom: 0;
    width: 264px;
    height: 168px;
    background: radial-gradient(circle at 100% 100%, rgba(220,180,110,0.85) 0%, rgba(220,180,110,0.55) 55%, rgba(220,180,110,0) 100%);
    border-top-left-radius: 100% 100%;
  }
  .crest {
    position: absolute;
    display: flex;
    align-items: center;
    justify-content: center;
    border-radius: 50%;
  }
  .crest__frame {
    position: absolute;
    inset: 0;
    border-radius: 50%;
    background: radial-gradient(circle, rgba(220,180,110,0) 58%, rgba(220,180,110,0.55) 64%, rgba(220,180,110,0.25) 90%, rgba(220,180,110,0) 100%);
  }
  .crest__seal {
    position: relative;
    display: flex;
    align-items: center;
    justify-content: center;
    border-radius: 50%;
  }
  .crest__initials {
    line-height: 1;
    white-space: nowrap;
  }
  .crest--card {
    left: 257px;
    top: 85px;
    width: 228px;
    height: 228px;
  }
  .crest--card .crest__seal {
    width: 142px;
    height: 142px;
    border: 2px solid var(--ivory);
  }
  .crest--card .crest__initials {
    color: var(--ivory);
    font-size: 58px;
  }
  .crest--standalone {
    left: 726px;
    top: 303px;
    width: 356px;
    height: 356px;
  }
  .crest--standalone .crest__seal {
    width: 200px;
    height: 200px;
    border: 2px solid var(--gold);
  }
  .crest--standalone .crest__initials {
    color: var(--gold);
    font-size: 80px;
  }
  .wording {
    position: absolute;
    left: 0;
    width: 600px;
    text-align: center;
    margin: 0;
    line-height: 1;
    font-weight: 400;
  }
  .wording--lead {
    top: 350px;
    color: var(--ivory);
    font-size: 21px;
  }
  .couple-names {
    top: 390px;
    color: var(--gold);
    font-size: 46px;
  }
  .couple-names .ampersand {
    color: var(--ivory);
    font-size: 36px;
  }
  .wording--detail {
    color: var(--ivory);
    font-size: 21px;
  }
  .detail-1 { top: 590px; }
  .detail-2 { top: 638px; }
  .detail-3 { top: 686px; }
  .detail-4 { top: 734px; }
  .detail-1, .detail-2, .detail-3, .detail-4 { top: auto; }
  .details {
    position: absolute;
    left: 0;
    top: 490px;
    width: 600px;
    margin: 0;
    text-align: center;
    color: var(--ivory);
    font-size: 21px;
  }
  .details p {
    margin: 0;
    height: 48px;
    line-height: 48px;
  }
  .venue {
    top: 706px;
    color: var(--gold);
    font-size: 21px;
  }
</style>
</head>
<body>
<main class="artboard">
  <section class="invitation">
    <div class="mehndi-corner mehndi-corner--top" role="img" aria-label="Gold mehndi-style floral and paisley ornament in the top left corner"></div>
    <div class="mehndi-corner mehndi-corner--bottom" role="img" aria-label="Gold mehndi-style floral and paisley ornament in the bottom right corner"></div>

    <div class="crest crest--card">
      <div class="crest__frame" role="img" aria-label="Gold filigree leaf wreath framing the couple's initials"></div>
      <div class="crest__seal"><span class="crest__initials">R&amp;M</span></div>
    </div>

    <p class="wording wording--lead">Together with their families</p>
    <h1 class="wording couple-names">Miranda <span class="ampersand">&amp;</span> Rohan</h1>

    <div class="details">
      <p>Invite you to celebrate their marriage</p>
      <p>Saturday, the twenty seventh of November</p>
      <p>at three o'clock in the afternoon</p>
      <p>Reception to follow</p>
    </div>

    <p class="wording venue">Willow Ridge</p>
  </section>

  <div class="crest crest--standalone">
    <div class="crest__frame" role="img" aria-label="Gold filigree leaf wreath framing the couple's initials"></div>
    <div class="crest__seal"><span class="crest__initials">R&amp;M</span></div>
  </div>
</main>
</body>
</html>
```